Industrial CNC laser cutting machine manufacturer needs a website designed

We need a website design for our company that re manufactures CNC laser cutting machines, we take old retired machines and completely re manufacture them from the ground up bringing them into the latest technology with all new parts and give them a new lease on life for a fraction of the cost of a new machine.

Machines can be fully customized to suit customers requirements too

My logo will need to be integrated and I want the website to look clean and modern

I will probably want 4 pages,Home, pictures, machines for sale and contact

```html
<!DOCTYPE html>
<html lang="en">
<head>
<meta charset="utf-8">
<title>Beamline Rebuild Works</title>
<link href="https://fonts.googleapis.com/css2?family=Rubik:wght@400;500;600&family=Mulish:wght@400;600;700;800&display=swap" rel="stylesheet">
<style>
:root{
  --red:#ed1c24;
  --ink:#222222;
  --grey-text:#7a7c80;
  --body:#555;
  --band:#ececec;
  --page:#fafafa;
  --dark:#2f2f2f;
  --white:#fff;
  --photo-a:#6d6f73;
  --photo-b:#c4c6c8;
  --orange:#d9602a;
  --hero-a:#23262b;
  --hero-b:#3a4049;
}
*{margin:0;padding:0;box-sizing:border-box}
html,body{width:1200px;height:3368px;overflow:hidden}
body{position:relative;background:var(--page);font-family:'Mulish',sans-serif;color:var(--body)}
.abs{position:absolute}
.btn{position:absolute;background:var(--red);color:var(--white);font:600 13px 'Rubik',sans-serif;display:flex;align-items:center;justify-content:center;text-transform:uppercase;letter-spacing:.2px}
.btn.grey{background:#7c7d80;font-size:10.5px}
.section-title{position:absolute;left:0;width:1200px;text-align:center;font:500 31px 'Rubik',sans-serif;color:var(--grey-text);text-transform:uppercase}
.section-title span{color:var(--red)}
.rule{position:absolute;width:76px;height:2px;background:#b8bcc2}
.photo{position:absolute;background:linear-gradient(150deg,var(--photo-b),var(--photo-a))}
.photo.warm{background:linear-gradient(160deg,#d8d8d6 0%,#b9b7b3 45%,var(--orange) 100%)}

/* header */
.site-header{position:absolute;left:0;top:0;width:1200px;height:80px;background:var(--white)}
.brand{position:absolute;left:141px;top:24px;display:flex;align-items:center;gap:10px;font:600 22px 'Rubik',sans-serif;color:var(--red)}
.brand i{width:26px;height:26px;background:#8a8c90;display:block}
.nav{position:absolute;left:521px;top:32px;display:flex;gap:32px;font:600 12px 'Rubik',sans-serif;color:var(--ink)}
.nav .active{color:var(--red)}
.nav-divider{position:absolute;left:883px;top:20px;width:1px;height:40px;background:#ddd}
.header-phone{position:absolute;left:911px;top:25px;display:flex;align-items:center;gap:12px;font:500 15px 'Rubik',sans-serif;color:var(--ink)}
.icon-circle{width:30px;height:30px;border-radius:50%;background:var(--red);display:flex;align-items:center;justify-content:center}

/* hero */
.hero{position:absolute;left:0;top:80px}
.hero-title{position:absolute;left:605px;top:183px;font:500 41px/49px 'Rubik',sans-serif;color:var(--white)}

/* about */
.about-photo-corner{position:absolute;left:133px;top:810px}
.about-heading{position:absolute;left:629px;top:828px;width:440px;font:600 20px/30px 'Mulish',sans-serif;color:var(--ink)}
.about-text{position:absolute;left:629px;top:895px;width:430px;font:400 14px/24px 'Mulish',sans-serif;color:#5f6064}

/* gallery */
.gallery-intro{position:absolute;left:225px;top:1396px;width:750px;text-align:center;font:400 16px/26px 'Mulish',sans-serif;color:#444}

/* machines */
.card{position:absolute;top:2231px;width:282px;height:378px;background:var(--white);box-shadow:0 2px 10px rgba(0,0,0,.06)}
.card .photo{left:0;top:0;width:282px;height:200px}
.card h3{position:absolute;left:19px;top:223px;font:500 15px 'Rubik',sans-serif;color:var(--red);text-transform:uppercase}
.card p{position:absolute;left:19px;top:249px;width:250px;font:400 12.5px/19px 'Mulish',sans-serif;color:#666}
.card .btn{left:19px;top:318px;width:106px;height:32px}
.arrow{position:absolute;top:2405px;width:46px;height:46px;border-radius:50%;background:var(--white);border:1px solid #e6c9c9;display:flex;align-items:center;justify-content:center}

/* contact */
.contact-title{position:absolute;left:141px;top:2924px;font:500 31px 'Rubik',sans-serif;color:var(--white)}
.contact-intro{position:absolute;left:143px;top:2991px;width:390px;font:400 16px/24px 'Mulish',sans-serif;color:#e5e5e5}
.info{position:absolute;left:143px;display:flex;gap:18px}
.info .icon-circle{width:42px;height:42px;flex:none}
.info b{display:block;font:600 13px 'Rubik',sans-serif;color:var(--white);margin-bottom:3px}
.info span{font:400 13px/17px 'Mulish',sans-serif;color:#e5e5e5}
.field{position:absolute;border:1px solid #8b8b8b;font:400 12.5px 'Mulish',sans-serif;color:#ddd;padding:15px 21px}
.copyright{position:absolute;left:143px;top:3331px;font:400 12px 'Mulish',sans-serif;color:#cfcfcf}
.copyright b{font-weight:800;color:var(--white)}
.social{position:absolute;top:3324px;width:28px;height:28px;border-radius:50%;background:var(--red)}
</style>
</head>
<body>

<header class="site-header">
  <div class="brand"><i></i>Beamline Rebuild Works</div>
  <nav class="nav"><span class="active">HOME</span><span>GALLERY</span><span>MACHINES</span><span>CONTACT US</span></nav>
  <div class="nav-divider"></div>
  <div class="header-phone">
    <div class="icon-circle"><svg width="14" height="14" viewBox="0 0 24 24" fill="none" stroke="#fff" stroke-width="2"><path d="M5 3h4l2 5-3 2a11 11 0 0 0 6 6l2-3 5 2v4a2 2 0 0 1-2 2A17 17 0 0 1 3 5a2 2 0 0 1 2-2z"/></svg></div>
    (555) 014-2290
  </div>
</header>

<section class="hero">
  <svg width="1200" height="580" viewBox="0 0 1200 580" role="img" aria-label="Photo of a CNC laser cutting head working on a metal sheet">
    <defs>
      <linearGradient id="heroShade" x1="0" y1="0" x2="1" y2="1">
        <stop offset="0" stop-color="#23262b"/>
        <stop offset="1" stop-color="#3a4049"/>
      </linearGradient>
    </defs>
    <polygon points="0,0 1200,0 1200,445 418,540 0,445" fill="url(#heroShade)"/>
    <polygon points="0,445 418,540 1200,445 1200,452 418,575 0,452" fill="#ed1c24"/>
  </svg>
  <h1 class="hero-title">We Are<br>Re-manufacture of CNC<br>Laser Cutting Machine</h1>
</section>

<h2 class="section-title" style="top:726px">About <span>Beamline</span> Rebuild <span>Works</span></h2>
<div class="rule" style="left:562px;top:777px"></div>

<svg class="about-photo-corner" width="212" height="140" viewBox="0 0 212 140"><polygon points="0,0 212,0 0,140" fill="#ed1c24"/></svg>
<div class="photo warm" style="left:141px;top:818px;width:436px;height:321px" role="img" aria-label="Photo of a rebuilt laser cutting machine in a workshop"></div>
<h3 class="about-heading">Lorem Ipsum Dolor Sit Amet Conser Adipicing Elit, Sed Diam Nonummy Nibh.</h3>
<p class="about-text">Lorem ipsum dolor sit amet, consectetuer adipiseing elit, sed diam nonummy nibh euismod tincidunt ut laoreet dolore mna aliquam erat volutpat. Ut wisi enim ad minim venim, quis nostrud exerci tation ullamcorper suscipit lobortis nisl ut ali ea codo consequat. Duis autem vel eum iriure dolor in hendrit in vulputate velit esse molestie consequat, vel illum dolore eu feugiat nulla facilisis at vero eros et accumsan et iusto odio dignissim.</p>
<div class="btn" style="left:629px;top:1078px;width:179px;height:43px">Contact us today</div>

<svg class="abs" style="left:0;top:1205px" width="1200" height="900" viewBox="0 0 1200 900">
  <polygon points="0,106 695,8 1200,106 1200,791 503,860 0,791" fill="#ececec"/>
  <polygon points="0,106 695,0 1200,106 1200,112 695,18 0,112" fill="#ed1c24"/>
  <polygon points="0,791 503,860 1200,791 1200,797 503,893 0,797" fill="#ed1c24"/>
</svg>

<h2 class="section-title" style="top:1326px">Our <span>Gallery</span></h2>
<div class="rule" style="left:562px;top:1376px"></div>
<p class="gallery-intro">Lorem ipsum dolor sit amet, consectetuer adipiseing elit, sed diam nonummy nibh euismod tincidunt ut laoreet dolore mna aliquam erat volutpat.wisi enim ad minim venim, quis.</p>

<div class="photo warm" style="left:141px;top:1470px;width:247px;height:206px" role="img" aria-label="Photo of a rebuilt laser machine, side view"></div>
<div class="photo warm" style="left:410px;top:1470px;width:378px;height:206px" role="img" aria-label="Photo of a machine cutting bed and enclosure"></div>
<div class="photo warm" style="left:810px;top:1470px;width:249px;height:206px" role="img" aria-label="Photo of a machine front with control console"></div>
<div class="photo" style="left:141px;top:1695px;width:247px;height:205px" role="img" aria-label="Photo of the inside of a machine enclosure with slat bed"></div>
<div class="photo warm" style="left:410px;top:1695px;width:247px;height:205px" role="img" aria-label="Photo of machine gantry and wiring during rebuild"></div>
<div class="photo warm" style="left:680px;top:1695px;width:379px;height:205px" role="img" aria-label="Close-up photo of a machine enclosure panel"></div>
<div class="btn" style="left:516px;top:1930px;width:168px;height:44px">View all gallery</div>

<h2 class="section-title" style="top:2149px">Machines <span>For Sale</span></h2>
<div class="rule" style="left:562px;top:2200px"></div>

<div class="card" style="left:141px"><div class="photo warm" role="img" aria-label="Photo of machine 1"></div><h3>Machine 1</h3><p>Lorem ipsum dolor sit amet consehcteter adipising elit, sed diam nonummy nibh euismod tincidunt ut laoreet.</p><div class="btn grey">View details</div></div>
<div class="card" style="left:459px"><div class="photo warm" role="img" aria-label="Photo of machine 2"></div><h3>Machine 2</h3><p>Lorem ipsum dolor sit amet consehcteter adipising elit, sed diam nonummy nibh euismod tincidunt ut laoreet.</p><div class="btn grey">View details</div></div>
<div class="card" style="left:777px"><div class="photo" role="img" aria-label="Photo of machine 3"></div><h3>Machine 3</h3><p>Lorem ipsum dolor sit amet consehcteter adipising elit, sed diam nonummy nibh euismod tincidunt ut laoreet.</p><div class="btn grey">View details</div></div>

<div class="arrow" style="left:51px"><svg width="16" height="16" viewBox="0 0 16 16" fill="none" stroke="#ed1c24" stroke-width="1.5"><path d="M14 8H2M7 3L2 8l5 5"/></svg></div>
<div class="arrow" style="left:1098px"><svg width="16" height="16" viewBox="0 0 16 16" fill="none" stroke="#ed1c24" stroke-width="1.5"><path d="M2 8h12M9 3l5 5-5 5"/></svg></div>
<div class="btn" style="left:510px;top:2638px;width:179px;height:43px">View all machines</div>

<svg class="abs" style="left:0;top:2750px" width="1200" height="618" viewBox="0 0 1200 618">
  <polygon points="0,112 782,24 1200,102 1200,618 0,618" fill="#2f2f2f"/>
  <polygon points="130,96 782,0 1130,90 782,26" fill="#ed1c24"/>
</svg>

<h2 class="contact-title">CONTACT US</h2>
<div class="rule" style="left:141px;top:2972px;background:#777"></div>
<p class="contact-intro">Lorem ipsum dolor sit amet, consectetuer adipiscing elit, sed diam nonummy nibh euismod.</p>

<div class="info" style="top:3063px">
  <div class="icon-circle"><svg width="20" height="20" viewBox="0 0 24 24" fill="none" stroke="#fff" stroke-width="1.8"><path d="M12 22s7-7 7-12a7 7 0 0 0-14 0c0 5 7 12 7 12z"/><circle cx="12" cy="10" r="2.5"/></svg></div>
  <div><b>ADDRESS</b><span>123 Lorem ipsum dolor sit amet,<br>consectetuer adipiscing.</span></div>
</div>
<div class="info" style="top:3142px">
  <div class="icon-circle"><svg width="20" height="20" viewBox="0 0 24 24" fill="none" stroke="#fff" stroke-width="1.8"><path d="M5 3h4l2 5-3 2a11 11 0 0 0 6 6l2-3 5 2v4a2 2 0 0 1-2 2A17 17 0 0 1 3 5a2 2 0 0 1 2-2z"/></svg></div>
  <div><b>PHONE</b><span>(555) 014-2290</span></div>
</div>
<div class="info" style="top:3204px">
  <div class="icon-circle"><svg width="20" height="20" viewBox="0 0 24 24" fill="none" stroke="#fff" stroke-width="1.8"><rect x="3" y="6" width="18" height="13" rx="1"/><path d="M3 7l9 7 9-7"/></svg></div>
  <div><b>EMAIL</b><span>info@beamlinerebuild.com</span></div>
</div>

<div class="field" style="left:619px;top:2929px;width:212px;height:44px">First Name*</div>
<div class="field" style="left:847px;top:2929px;width:212px;height:44px">Last Name*</div>
<div class="field" style="left:619px;top:2991px;width:212px;height:44px">Phone*</div>
<div class="field" style="left:847px;top:2991px;width:212px;height:44px">Email*</div>
<div class="field" style="left:619px;top:3052px;width:440px;height:127px">Message</div>
<div class="btn" style="left:619px;top:3201px;width:139px;height:42px">Submit now</div>

<p class="copyright">Copyright © 2020 <b>BEAMLINE REBUILD WORKS.</b> All Rights Reserved.</p>
<div class="social" style="left:925px" role="img" aria-label="Social link"></div>
<div class="social" style="left:960px" role="img" aria-label="Social link"></div>
<div class="social" style="left:995px" role="img" aria-label="Social link"></div>
<div class="social" style="left:1030px" role="img" aria-label="Social link"></div>

</body>
</html>
```